Lumora Vitality MediSpa Brochure

We need a new brochure design. The old is attached.

We are wanting a three panel brochure for med spa designed and ready for print. The brochure will have content and images on both sides. We attached the old brochure in pdf format. The content needs to stay as on the attached pdf but please feel free to offer new designs. The color needs to match the attached logo, which is a light blue and teal. All images we want on the brochure are also attached.

The design must have an 1/8 in space from each edge for printing purposes

Target Market(s)

Men and Women

Industry/Entity Type

Wellness

Font styles to use
Sans Serif

Colors
34a6d7
33b8a4

Requirements
Must have
• soft curves. must have a 1/8 in space on all edges (including interior) to give bleed space for printing. Use content written on attached brochure.

```html
<!DOCTYPE html>
<html lang="en">
<head>
<meta charset="utf-8">
<title>Lumora Vitality MediSpa Brochure</title>
<link rel="stylesheet" href="https://fonts.googleapis.com/css2?family=Open+Sans:ital,wght@0,400;0,600;0,700;1,400&family=Roboto+Condensed:ital,wght@0,700;1,700&display=swap">
<style>
:root{
  --blue:#34a6d7;
  --blue-light:#45bdf0;
  --teal:#33b8a4;
  --teal-deep:#1fa6a6;
  --ink:#2b2b2b;
  --muted:#555;
  --paper:#ffffff;
  --stage:#d9dbde;
}
*{box-sizing:border-box;margin:0;padding:0}
html,body{width:1200px;height:1200px;overflow:hidden;background:var(--stage)}
body{font-family:"Open Sans",sans-serif;color:var(--ink);position:relative}
.brochure{position:absolute;left:30px;top:160px;width:1140px;height:880px;display:flex;box-shadow:0 10px 30px rgba(0,0,0,.18)}
.panel{position:relative;width:380px;height:880px;background:var(--paper);overflow:hidden}
.panel + .panel{border-left:1px solid #e4e6e8}
.panel-bg{position:absolute;inset:0}
.brand{position:absolute;left:0;right:0;text-align:center;font-family:"Open Sans",sans-serif;font-weight:600;color:var(--teal-deep);display:flex;align-items:center;justify-content:center;gap:10px}
.brand-dot{width:14px;height:14px;border-radius:50%;background:var(--teal)}
.pill{position:absolute;background:#fff;border-radius:0 22px 22px 0;font-family:"Roboto Condensed",sans-serif;font-weight:700;font-style:italic;text-transform:uppercase;color:var(--ink);box-shadow:0 3px 6px rgba(0,0,0,.15);display:flex;align-items:center}
.copy{position:absolute;color:#fff;font-size:12.5px;line-height:1.5;font-style:italic}
/* left panel */
.left .brand{top:62px;font-size:19px}
.left .pill{left:0;height:40px;padding:0 26px 0 30px;font-size:17px}
.membership-list{position:absolute;left:30px;top:700px;list-style:none;color:#fff;font-size:14px;font-style:italic}
.membership-list li{display:flex;align-items:center;gap:8px;margin-bottom:4px}
.left-footer{position:absolute;left:0;right:0;top:820px;text-align:center;font-size:11.5px;color:var(--muted);line-height:1.5}
/* middle panel */
.portrait{position:absolute;left:105px;top:36px;width:170px;height:170px;border-radius:50%;border:8px solid var(--teal);box-shadow:0 0 0 4px #fff,0 3px 10px rgba(0,0,0,.2);background:radial-gradient(circle at 50% 40%,#c99a7e 0%,#6b4a3a 35%,#3f6b34 70%,#2d4e26 100%)}
.card{position:absolute;left:24px;right:24px;border:1.5px solid #9a9a9a;border-radius:24px;background:#fff}
.bio{top:236px;height:326px;padding:22px 22px}
.bio h2{font-family:"Roboto Condensed",sans-serif;font-style:italic;font-weight:700;color:var(--teal-deep);font-size:19px;text-align:center;margin-bottom:14px}
.bio p{font-size:12.5px;line-height:1.45;font-style:italic;margin-bottom:12px}
.location{top:590px;height:258px;padding:22px 24px;text-align:center}
.location h2{font-family:"Roboto Condensed",sans-serif;font-weight:700;color:var(--teal-deep);font-size:20px;margin-bottom:12px;text-transform:uppercase}
.contact{list-style:none;font-size:13px;line-height:1.5;display:inline-block;text-align:left}
.contact li{display:flex;gap:8px;align-items:flex-start}
.contact svg{flex:none;margin-top:4px}
.contact .lead{font-size:15px;margin:6px 0 2px}
/* right panel */
.tagline{position:absolute;left:36px;top:18px;color:#fff;font-family:"Roboto Condensed",sans-serif;font-weight:700;font-size:21px;letter-spacing:.5px;text-transform:uppercase}
.right .brand{top:100px;font-size:22px}
.hero{position:absolute;left:70px;right:0;top:180px;height:440px;background:linear-gradient(160deg,#f6e3d8 0%,#ebc7b3 45%,#d9a994 80%,#f3e6df 100%)}
.audience{position:absolute;left:0;top:620px;height:46px;padding:0 34px 0 40px;font-size:22px;color:var(--teal-deep)}
.services{position:absolute;list-style:none;color:#fff;font-size:17px;line-height:1.35}
.services li{display:flex;align-items:center;gap:8px}
.services-a{left:34px;top:690px}
.services-b{left:190px;top:740px}
.right-footer{position:absolute;left:0;right:0;top:836px;display:flex;justify-content:space-between;padding:0 26px;font-size:12.5px;color:var(--muted)}
.right-footer span{display:flex;align-items:center;gap:6px}
</style>
</head>
<body>
<main class="brochure">

  <section class="panel left">
    <svg class="panel-bg" width="380" height="880" viewBox="0 0 380 880" aria-hidden="true">
      <defs>
        <linearGradient id="leftBlue" x1="0" y1="0" x2="1" y2="1">
          <stop offset="0" stop-color="#34a6d7"/>
          <stop offset="1" stop-color="#45bdf0"/>
        </linearGradient>
      </defs>
      <path d="M0 170 Q190 140 380 160 L380 790 Q190 820 0 780 Z" fill="url(#leftBlue)"/>
    </svg>
    <div class="brand"><span class="brand-dot"></span>Lumora Vitality MediSpa</div>

    <div class="pill" style="top:170px">Brightvale's Premier MediSpa</div>
    <p class="copy" style="left:30px;right:30px;top:228px">Lumora Vitality MediSpa is the premier medical spa in Brightvale, TX. We utilize the best equipment available today for laser treatments, dermal fillers, facials, injections, chemical peels and wellness solutions.</p>

    <div class="pill" style="top:340px">Why Choose Our MediSpa?</div>
    <p class="copy" style="left:30px;right:30px;top:398px">Under the supervision of Dr. Elena Hartwell, our medical staff provides state-of-the-art cosmetic treatments to both women and men.</p>
    <p class="copy" style="left:30px;right:30px;top:468px">Our staff is trained to provide unique medical spa services to help our clients achieve a more youthful look and defy the aging process.</p>

    <div class="pill" style="top:570px">Exclusive Memberships</div>
    <p class="copy" style="left:30px;right:30px;top:626px">Our exclusive membership packages are tailored for our clients and created to give them an exceptional experience at a discounted price.</p>
    <ul class="membership-list">
      <li><svg width="13" height="13" viewBox="0 0 13 13"><rect x="1" y="1" width="11" height="11" rx="2" fill="none" stroke="#fff" stroke-width="1.4"/><path d="M3.5 6.5l2 2 4-5" fill="none" stroke="#fff" stroke-width="1.6"/></svg>SILVER Membership</li>
      <li><svg width="13" height="13" viewBox="0 0 13 13"><rect x="1" y="1" width="11" height="11" rx="2" fill="none" stroke="#fff" stroke-width="1.4"/><path d="M3.5 6.5l2 2 4-5" fill="none" stroke="#fff" stroke-width="1.6"/></svg>GOLD Membership</li>
      <li><svg width="13" height="13" viewBox="0 0 13 13"><rect x="1" y="1" width="11" height="11" rx="2" fill="none" stroke="#fff" stroke-width="1.4"/><path d="M3.5 6.5l2 2 4-5" fill="none" stroke="#fff" stroke-width="1.6"/></svg>PLATINUM Membership</li>
    </ul>
    <p class="left-footer">Learn More at<br>www.LumoraVitalityMedispa.com/memberships</p>
  </section>

  <section class="panel middle">
    <div class="portrait" role="img" aria-label="Portrait photo of the physician outdoors"></div>

    <article class="card bio">
      <h2>DR. ELENA HARTWELL, MD FACS</h2>
      <p>“Rejuvenation and reconstruction of the face are my passion, whether it is to improve one's visual functions or to enhance one's appearance.”</p>
      <p>“I personally perform all of my injections and Co2 laser treatments because safety and satisfaction are my top priorities.”</p>
      <p>“I was called by God to become a physician at the age of seven years old. I am motivated by a desire to serve others by providing superb medical care. I constantly strive to do my best.”</p>
    </article>

    <article class="card location">
      <h2>Location</h2>
      <ul class="contact">
        <li><svg width="11" height="14" viewBox="0 0 11 14"><path d="M5.5 0C2.5 0 0 2.4 0 5.3 0 9 5.5 14 5.5 14S11 9 11 5.3C11 2.4 8.5 0 5.5 0z" fill="#222"/><circle cx="5.5" cy="5.3" r="2" fill="#fff"/></svg><span>418 W Meadowbrook Ave<br>Suite 210<br>Brightvale TX 75501</span></li>
        <li class="lead"><span>Schedule a consultation</span></li>
        <li><svg width="12" height="12" viewBox="0 0 12 12"><rect width="12" height="12" rx="2" fill="#222"/><path d="M3.5 2.5l1.5 1.5-1 1a5 5 0 0 0 3 3l1-1 1.5 1.5-1 1.5c-3 0-6-3-6-6z" fill="#fff"/></svg><span>(555) 214-7730</span></li>
        <li><svg width="12" height="12" viewBox="0 0 12 12"><rect width="12" height="12" rx="2" fill="#222"/><rect x="2.5" y="3" width="7" height="6" fill="#fff"/></svg><span>(555) 318-4492</span></li>
        <li><svg width="12" height="10" viewBox="0 0 12 10"><rect width="12" height="10" rx="1" fill="#222"/><path d="M1 1l5 4 5-4" fill="none" stroke="#fff" stroke-width="1.2"/></svg><span>glow@elenahartwellmd.com</span></li>
        <li><svg width="12" height="12" viewBox="0 0 12 12"><circle cx="6" cy="6" r="6" fill="#222"/><path d="M0.5 6h11M6 0.5c-2.5 3-2.5 8 0 11M6 0.5c2.5 3 2.5 8 0 11" fill="none" stroke="#fff" stroke-width=".9"/></svg><span>www.LumoraVitalityMedispa.com</span></li>
      </ul>
    </article>
  </section>

  <section class="panel right">
    <svg class="panel-bg" width="380" height="880" viewBox="0 0 380 880" aria-hidden="true">
      <path d="M0 0 H380 V70 Q190 62 0 80 Z" fill="#34a6d7"/>
      <path d="M10 160 Q200 150 380 200" fill="none" stroke="#1fa6a6" stroke-width="4"/>
      <path d="M0 600 Q40 610 70 620 Q220 650 380 612 V880 H0 Z" fill="#1fb3b0"/>
      <path d="M0 826 Q190 812 380 824 V880 H0 Z" fill="#fff"/>
    </svg>
    <div class="tagline">Refresh and Rejuvenate</div>
    <div class="brand"><span class="brand-dot"></span>Lumora Vitality MediSpa</div>
    <div class="hero" role="img" aria-label="Close-up photo of a woman's face with smooth, radiant skin"></div>
    <svg style="position:absolute;left:0;top:600px" width="380" height="60" viewBox="0 0 380 60" aria-hidden="true"><path d="M0 0 Q40 10 70 20 Q220 50 380 12 V60 H0 Z" fill="#1fb3b0"/></svg>

    <div class="pill audience">For Women and Men</div>
    <ul class="services services-a">
      <li><svg width="14" height="14" viewBox="0 0 13 13"><rect x="1" y="1" width="11" height="11" rx="2" fill="none" stroke="#fff" stroke-width="1.4"/><path d="M3.5 6.5l2 2 4-5" fill="none" stroke="#fff" stroke-width="1.6"/></svg>Laser Treatments</li>
      <li><svg width="14" height="14" viewBox="0 0 13 13"><rect x="1" y="1" width="11" height="11" rx="2" fill="none" stroke="#fff" stroke-width="1.4"/><path d="M3.5 6.5l2 2 4-5" fill="none" stroke="#fff" stroke-width="1.6"/></svg>Dermal Fillers</li>
      <li><svg width="14" height="14" viewBox="0 0 13 13"><rect x="1" y="1" width="11" height="11" rx="2" fill="none" stroke="#fff" stroke-width="1.4"/><path d="M3.5 6.5l2 2 4-5" fill="none" stroke="#fff" stroke-width="1.6"/></svg>Neurotoxins</li>
    </ul>
    <ul class="services services-b">
      <li><svg width="14" height="14" viewBox="0 0 13 13"><rect x="1" y="1" width="11" height="11" rx="2" fill="none" stroke="#fff" stroke-width="1.4"/><path d="M3.5 6.5l2 2 4-5" fill="none" stroke="#fff" stroke-width="1.6"/></svg>Facials</li>
      <li><svg width="14" height="14" viewBox="0 0 13 13"><rect x="1" y="1" width="11" height="11" rx="2" fill="none" stroke="#fff" stroke-width="1.4"/><path d="M3.5 6.5l2 2 4-5" fill="none" stroke="#fff" stroke-width="1.6"/></svg>Chemical Peels</li>
      <li><svg width="14" height="14" viewBox="0 0 13 13"><rect x="1" y="1" width="11" height="11" rx="2" fill="none" stroke="#fff" stroke-width="1.4"/><path d="M3.5 6.5l2 2 4-5" fill="none" stroke="#fff" stroke-width="1.6"/></svg>Wellness Treatments</li>
    </ul>

    <div class="right-footer">
      <span><svg width="12" height="12" viewBox="0 0 12 12"><circle cx="6" cy="6" r="6" fill="#33b8a4"/><path d="M0.5 6h11M6 0.5c-2.5 3-2.5 8 0 11M6 0.5c2.5 3 2.5 8 0 11" fill="none" stroke="#fff" stroke-width=".9"/></svg>www.LumoraVitalityMedispa.com</span>
      <span><svg width="10" height="14" viewBox="0 0 10 14"><path d="M2 1l2 3-1.5 1.5a7 7 0 0 0 3 4L7 8l2.5 2.5L8 13C4 13 0 8 1 2z" fill="#33b8a4"/></svg>(555) 214-7730</span>
    </div>
  </section>

</main>
</body>
</html>
```